A website for a Maltese Law Firm

Our law firm needs a website to further its business. The site should have a simple yet effective design. We would need the following sections: About us, Practice Areas, About Malta, Contact. These should be further split as follows:

About us: Our firm, Our values, What others say, Offices

Practice Areas: Crimimal, Citizenship & Residence, Harbour Passage Scheme, Criminal Defence, Civil Litigation, Arbitration and ADR, Commercial and Corporate, Media Law.

About Malta: just one section.

Contact: Just one section

We would also need a news feed at the front of the site to include latest news regarding our cases.

At the bottom we need a section for our Terms and a Privacy Statement.

Our logo is being attached.

Target Market(s)

All clients looking for legal assistance in Malta

Industry/Entity Type

Legal

Coding

Coded - Design and coding required

Number of Pages Required

1 page

Requirements
Must have
• It must be simple yet striking.

```html
<!DOCTYPE html>
<html lang="en">
<head>
<meta charset="utf-8">
<title>Falzon &amp; Grech Advocates</title>
<link rel="stylesheet" href="https://fonts.googleapis.com/css2?family=Cinzel:wght@400;700&family=Arimo:ital,wght@0,400;0,700;1,400&family=Roboto+Condensed:wght@400&display=swap">
<style>
:root{
  --ink:#1a1a1a;
  --text:#444;
  --muted:#777;
  --topbar:#575757;
  --black:#000;
  --white:#fff;
  --soft:#efefef;
  --footer:#e4e4e4;
  --line:#cfcfcf;
  --serif:'Cinzel', serif;
  --sans:'Arimo', sans-serif;
  --cond:'Roboto Condensed', sans-serif;
}
*{box-sizing:border-box;margin:0;padding:0}
html,body{width:1200px;height:2413px;overflow:hidden}
body{position:relative;background:var(--white);font-family:var(--sans);color:var(--text)}
.abs{position:absolute}
.section{position:absolute;left:0;width:1200px}

/* top bar */
.topbar{top:0;height:35px;background:var(--topbar)}
.social{position:absolute;top:8px;width:19px;height:19px;border:1px solid #ddd}
.topbar .contact{position:absolute;top:0;height:35px;display:flex;align-items:center;gap:10px;color:var(--white);font-size:13px}
.topbar .icon{width:24px;height:20px;background:var(--white);display:flex;align-items:center;justify-content:center}

/* header */
.header{top:35px;height:110px;background:var(--white)}
.brand{position:absolute;left:80px;top:38px;font-family:var(--serif);font-size:30px;color:var(--ink);letter-spacing:0.5px}
.cta{position:absolute;left:843px;top:8px;width:278px;height:37px;background:var(--black);color:var(--white);font-family:var(--serif);font-size:16px;display:flex;align-items:center;justify-content:center}
.nav{position:absolute;right:79px;top:62px;display:flex;font-family:var(--serif);font-size:13.5px;color:#777}
.nav span{padding:0 10px;border-left:1px solid #bbb;line-height:16px}
.nav span:first-child{border-left:0;color:var(--ink)}
.nav span:last-child{padding-right:0}

/* hero */
.hero{top:145px;height:508px;background:radial-gradient(ellipse at 70% 40%,#a8682e 0%,#6b3a17 45%,#2b1608 100%)}
.hero-caption{position:absolute;left:130px;top:182px;width:547px;height:143px;background:rgba(0,0,0,.62);padding:14px 13px}
.hero-caption h1{font-family:var(--serif);font-weight:400;font-size:30px;color:var(--white);letter-spacing:.5px}
.hero-caption p{font-size:12px;color:#eee;line-height:19px;margin-top:6px}
.btn-light{display:inline-block;margin-top:12px;background:#d7d7d7;color:var(--ink);font-weight:700;font-size:13px;padding:6px 20px}
.slide-arrow{position:absolute;top:237px;width:30px;height:30px;border-radius:50%;display:flex;align-items:center;justify-content:center}

/* about */
.about{top:653px;height:306px;text-align:center}
.section-title{font-family:var(--serif);font-weight:400;font-size:28px;color:var(--ink)}
.about .section-title{position:absolute;top:48px;width:100%}
.about p{position:absolute;left:92px;width:1016px;font-size:12.5px;line-height:19px;color:#333}
.btn-dark{display:flex;align-items:center;justify-content:center;background:var(--black);color:var(--white);font-weight:700;font-size:13px}

/* practice */
.practice{top:959px;height:397px;background:linear-gradient(180deg,#39424c 0%,#4a4440 45%,#2b2622 100%)}
.practice .section-title{position:absolute;left:80px;top:20px;color:var(--white)}
.practice .rule{position:absolute;left:80px;top:58px;width:676px;height:1px;background:rgba(255,255,255,.35)}
.area{position:absolute;display:flex;align-items:center;gap:14px;color:var(--white);font-family:Georgia,serif;font-size:16px}
.area .glyph{width:39px;height:39px;border:1.5px solid var(--white);display:flex;align-items:center;justify-content:center}
.call{position:absolute;left:80px;top:327px;font-family:var(--cond);font-size:22px;color:var(--white)}
.request{position:absolute;left:814px;top:22px;width:302px;height:325px;background:rgba(120,120,120,.55)}
.request h2{position:absolute;left:11px;top:6px;font-family:var(--serif);font-size:19px;line-height:21px;color:var(--white);font-weight:700}
.field{position:absolute;left:13px;width:276px;background:rgba(150,150,150,.75);color:var(--white);font-size:12px;padding:9px 10px;border:1px solid rgba(255,255,255,.25)}
.submit{position:absolute;left:16px;top:285px;width:101px;height:29px}

/* testimonials */
.reviews{top:1356px;height:357px;background:var(--soft);text-align:center}
.reviews .section-title{position:absolute;top:63px;width:100%}
.reviews .rule{position:absolute;left:394px;top:101px;width:415px;height:1px;background:#999}
.avatar{position:absolute;left:124px;top:124px;width:108px;height:108px;border-radius:50%;background:linear-gradient(180deg,#c7b09c,#8f7a6a);border:4px solid var(--white)}
.quote-mark{position:absolute;left:268px;top:124px;font-family:Georgia,serif;font-size:40px;color:#aaa;line-height:1}
.quote{position:absolute;left:267px;top:140px;width:812px;text-align:left;font-style:italic;font-size:12.5px;line-height:22.5px;color:#333;text-indent:32px}
.author{position:absolute;left:270px;top:252px;font-style:italic;font-weight:700;font-size:12px;color:var(--ink)}
.pager{position:absolute;width:20px;height:18px;border:1.5px solid #333;display:flex;align-items:center;justify-content:center;background:var(--white)}

/* case study */
.cases{top:1713px;height:399px}
.cases .section-title{position:absolute;left:80px;top:48px}
.cases .rule{position:absolute;left:80px;top:85px;width:177px;height:1px;background:#999}
.case-photo{position:absolute;top:116px;width:216px;height:216px}
.case-body{position:absolute;top:116px;width:259px}
.case-body h3{font-size:14.5px;line-height:22px;color:var(--ink);padding-bottom:8px;border-bottom:1px solid #ddd}
.case-body p{font-size:13px;line-height:19px;color:#444;margin-top:8px}
.case-body time{display:block;margin-top:10px;font-style:italic;font-size:12.5px;color:#777}
.case-body .btn-dark{margin-top:12px;width:87px;height:29px}

/* footer */
.footer{top:2112px;height:269px;background:var(--footer)}
.follow{position:absolute;left:88px;top:-13px;width:211px;height:38px;background:var(--black);display:flex;align-items:center;gap:8px;padding-left:18px;color:var(--white);font-size:12px}
.follow i{width:19px;height:19px;border:1px solid #ccc;display:block}
.follow i:first-of-type{margin-left:8px}
.col-title{position:absolute;top:55px;font-family:var(--serif);font-size:14.5px;color:var(--ink);padding-bottom:8px;border-bottom:1px solid var(--line)}
.links{position:absolute;left:85px;top:100px;list-style:none;font-size:12px;color:#333}
.links li{height:22.4px;padding-left:17px;position:relative}
.links li::before{content:"›";position:absolute;left:0;top:-2px;color:#888}
.details{position:absolute;left:310px;top:97px;font-size:12px;color:#333}
.details .row{position:absolute;left:0;display:flex;gap:12px;white-space:nowrap;line-height:17px}
.details .ic{width:16px;height:16px;background:var(--ink);flex:none}
.map{position:absolute;left:587px;top:60px;width:262px;height:170px;background:linear-gradient(135deg,#cfd6c8 0%,#dcd9cf 50%,#a9c4da 100%);border:2px solid #bbb}
.footer-brand{position:absolute;left:893px;top:18px;font-family:var(--serif);font-size:19px;color:#555}
.hours-intro{position:absolute;left:893px;top:98px;width:228px;font-size:11.5px;line-height:18px;color:#333}
.hours{position:absolute;left:893px;width:228px;display:flex;justify-content:space-between;font-size:11.5px;color:#333;padding-bottom:10px;border-bottom:1px solid var(--line)}
.copyright{top:2381px;height:32px;background:var(--black)}
.copyright .strip{position:absolute;left:0;top:0;width:1200px;height:17px;background:var(--footer);display:flex;align-items:center;justify-content:center;gap:12px;font-size:11.5px;color:#333}
.copyright .strip b{display:block;width:180px;height:1px;background:#999}
</style>
</head>
<body>

<header>
  <div class="section topbar">
    <span class="social" style="left:80px"></span>
    <span class="social" style="left:109px"></span>
    <span class="social" style="left:138px"></span>
    <span class="social" style="left:167px"></span>
    <div class="contact" style="left:770px">
      <span class="icon"><svg width="12" height="12" viewBox="0 0 24 24"><path fill="#555" d="M6.6 10.8a15 15 0 0 0 6.6 6.6l2.2-2.2c.3-.3.7-.4 1-.2 1.1.4 2.3.6 3.6.6.6 0 1 .4 1 1V20c0 .6-.4 1-1 1A17 17 0 0 1 3 4c0-.6.4-1 1-1h3.5c.6 0 1 .4 1 1 0 1.3.2 2.5.6 3.6.1.3 0 .7-.2 1z"/></svg></span>
      <span>356 2000 1100</span>
    </div>
    <div class="contact" style="left:910px">
      <span class="icon"><svg width="13" height="10" viewBox="0 0 26 20"><rect x="1" y="1" width="24" height="18" fill="none" stroke="#555" stroke-width="2"/><path d="M1 1l12 10L25 1" fill="none" stroke="#555" stroke-width="2"/></svg></span>
      <span>office@fgadvocates.com</span>
    </div>
  </div>

  <div class="section header">
    <div class="brand">Falzon &amp; Grech</div>
    <div class="cta">Schedule Free Consultation</div>
    <nav class="nav">
      <span>Home</span><span>About Us</span><span>Our Firm</span><span>Our Values</span><span>What Others Say</span><span>Offices</span><span>Contact Us</span>
    </nav>
  </div>
</header>

<section class="section hero" role="img" aria-label="Brass scales of justice on a wooden desk in a law library">
  <div class="hero-caption">
    <h1>Get Qualified Legal Advice</h1>
    <p>Lorem ipsum dolor sit amet, consectetuer adipiscing elit, sed diam nonummy nibh euismod tincidunt ut laoreet dolore magna aliquam erat volutpat.</p>
    <span class="btn-light">Read More</span>
  </div>
  <span class="slide-arrow" style="left:35px;background:var(--white)"><svg width="10" height="12" viewBox="0 0 10 12"><path d="M7 1L2 6l5 5" fill="none" stroke="#000" stroke-width="2"/></svg></span>
  <span class="slide-arrow" style="left:1134px;background:var(--black)"><svg width="10" height="12" viewBox="0 0 10 12"><path d="M3 1l5 5-5 5" fill="none" stroke="#fff" stroke-width="2"/></svg></span>
</section>

<section class="section about">
  <h2 class="section-title">About Falzon &amp; Grech</h2>
  <p style="top:106px">Lorem ipsum dolor sit amet, consectetuer adipiscing elit, sed diam nonummy nibh euismod tincidunt ut laoreet dolore magna aliquam erat volutpat. Ut wisi enim ad minim veniam, quis nostrud exerci tation ullamcorper suscipit lobortis nisl ut aliquip ex ea commodo consequat. Duis autem vel eum iriure dolor in hendrerit in vulputate velit esse molestie consequat, vel illum dolore eu feugiat nulla facilisis at vero eros et accumsan et iusto odio dignissim qui blandit praesent luptatum zzril delenit augue duis dolore te feugait nulla facilisi.</p>
  <p style="top:177px">Lorem ipsum dolor sit amet, consectetuer adipiscing elit, sed diam nonummy nibh euismod tincidunt ut laoreet dolore magna aliquam erat volutpat. Ut wisi enim ad minim veniam, quis nostrud exerci tation ullamcorper suscipit lobortis nisl ut aliquip ex ea commodo consequat. Duis autem vel eum iriure dolor in hendrerit in vulputate velit esse molestie consequat,</p>
  <span class="btn-dark abs" style="left:549px;top:235px;width:102px;height:29px">Read More</span>
</section>

<section class="section practice" role="img" aria-label="Evening view of a Maltese city skyline with a domed church">
  <h2 class="section-title">Our Practice Areas</h2>
  <div class="rule"></div>

  <div class="area" style="left:80px;top:87px"><span class="glyph"><svg width="20" height="20"><circle cx="10" cy="10" r="6" fill="none" stroke="#fff" stroke-width="1.5"/></svg></span>Crimimal Law</div>
  <div class="area" style="left:80px;top:145px"><span class="glyph"><svg width="20" height="20"><circle cx="10" cy="10" r="6" fill="none" stroke="#fff" stroke-width="1.5"/></svg></span>Citizenship &amp; Residence</div>
  <div class="area" style="left:80px;top:204px"><span class="glyph"><svg width="20" height="20"><circle cx="10" cy="10" r="6" fill="none" stroke="#fff" stroke-width="1.5"/></svg></span>Harbour Passage Scheme</div>
  <div class="area" style="left:80px;top:264px"><span class="glyph"><svg width="20" height="20"><circle cx="10" cy="10" r="6" fill="none" stroke="#fff" stroke-width="1.5"/></svg></span>Commercial &amp; Corporate</div>

  <div class="area" style="left:470px;top:87px"><span class="glyph"><svg width="20" height="20"><circle cx="10" cy="10" r="6" fill="none" stroke="#fff" stroke-width="1.5"/></svg></span>Criminal Defence</div>
  <div class="area" style="left:470px;top:145px"><span class="glyph"><svg width="20" height="20"><circle cx="10" cy="10" r="6" fill="none" stroke="#fff" stroke-width="1.5"/></svg></span>Civil Litigation</div>
  <div class="area" style="left:470px;top:204px"><span class="glyph"><svg width="20" height="20"><circle cx="10" cy="10" r="6" fill="none" stroke="#fff" stroke-width="1.5"/></svg></span>Arbitration &amp; ADR</div>
  <div class="area" style="left:470px;top:264px"><span class="glyph"><svg width="20" height="20"><circle cx="10" cy="10" r="6" fill="none" stroke="#fff" stroke-width="1.5"/></svg></span>Media Law</div>

  <p class="call">Call us 356 2000 1100 &nbsp;at &nbsp;or contact us online for a Free estimate</p>

  <form class="request">
    <h2>Request for Free<br>Consulatation</h2>
    <div class="field" style="top:76px;height:35px">Name</div>
    <div class="field" style="top:121px;height:35px">Email</div>
    <div class="field" style="top:164px;height:37px;display:flex;justify-content:space-between"><span>Inquiry Tpye</span><span>V</span></div>
    <div class="field" style="top:209px;height:61px">Message</div>
    <span class="btn-dark submit">SUBMIT</span>
  </form>
</section>

<section class="section reviews">
  <h2 class="section-title">What Other's Say About Us</h2>
  <div class="rule"></div>
  <div class="avatar" role="img" aria-label="Portrait of a client"></div>
  <span class="quote-mark">&#8220;</span>
  <p class="quote">Lorem ipsum dolor sit amet, consectetuer adipiscing elit, sed diam nonummy nibh euismod tincidunt ut laoreet dolore magna aliquam erat volutpat. Ut wisi enim ad minim veniam, quis nostrud exerci tation ullamcorper suscipit lobortis nisl ut aliquip commodo consequat. Duis autem vel eum iriure dolor in hendrerit in vulputate velit esse molestie consequat, vel illum dolore eu feugiat nulla facilisis at vero eros et accumsan et iusto odio dignissimaugue duis dolore te feugait nulla facilisi.</p>
  <p class="author">.... Lorem Ispum, Manger</p>
  <span class="pager" style="left:574px;top:285px"><svg width="8" height="10"><path d="M6 1L2 5l4 4" fill="none" stroke="#000" stroke-width="1.5"/></svg></span>
  <span class="pager" style="left:604px;top:285px"><svg width="8" height="10"><path d="M2 1l4 4-4 4" fill="none" stroke="#000" stroke-width="1.5"/></svg></span>
</section>

<section class="section cases">
  <h2 class="section-title">Case Study</h2>
  <div class="rule"></div>
  <span class="pager" style="left:1065px;top:61px"><svg width="8" height="10"><path d="M6 1L2 5l4 4" fill="none" stroke="#000" stroke-width="1.5"/></svg></span>
  <span class="pager" style="left:1096px;top:61px"><svg width="8" height="10"><path d="M2 1l4 4-4 4" fill="none" stroke="#000" stroke-width="1.5"/></svg></span>

  <div class="case-photo" style="left:80px;background:linear-gradient(160deg,#6b3b1d,#b17a45 60%,#d9c3a6)" role="img" aria-label="Two lawyers reviewing documents at a table"></div>
  <article class="case-body" style="left:317px">
    <h3>Ut wisi enim ad minim veniam quis nostrud exerci tation</h3>
    <p>Lorem ipsum dolor sit amet, consectetuer adipiscing elit, sed diam nonummy nibh euismod tincidunt ut laoreet dolore magna aliquam erat volutpat.</p>
    <time>2014-11-26-23:14:43</time>
    <span class="btn-dark">Read More</span>
  </article>

  <div class="case-photo" style="left:621px;background:linear-gradient(160deg,#e9e9e9,#9a8a78 55%,#2d2a28)" role="img" aria-label="Lawyer writing at a desk beside a justice statue"></div>
  <article class="case-body" style="left:861px">
    <h3>Ut wisi enim ad minim veniam quis nostrud exerci tation</h3>
    <p>Lorem ipsum dolor sit amet, consectetuer adipiscing elit, sed diam nonummy nibh euismod tincidunt ut laoreet dolore magna aliquam erat volutpat.</p>
    <time>2014-11-26-23:14:43</time>
    <span class="btn-dark">Read More</span>
  </article>
</section>

<footer class="section footer">
  <div class="follow">Follow us <i></i><i></i><i></i><i></i></div>

  <h4 class="col-title" style="left:85px;width:178px">Quick Links</h4>
  <ul class="links">
    <li>Home</li><li>About Us</li><li>Our Firm</li><li>Our Values</li><li>What Others Say</li><li>Offices</li><li>Contact Us</li>
  </ul>

  <h4 class="col-title" style="left:310px;width:196px">Contact Details</h4>
  <div class="details">
    <div class="row" style="top:0"><span class="ic"></span><span>12, Merchant Row, Valletta<br>88, Orchard Lane, Birkirkara</span></div>
    <div class="row" style="top:45px"><span class="ic"></span><span>356 2000 1100 ( Valletta )</span></div>
    <div class="row" style="top:69px"><span class="ic"></span><span>356 2000 2200 (Birkirkara )</span></div>
    <div class="row" style="top:95px"><span class="ic"></span><span>office@fgadvocates.com</span></div>
  </div>

  <div class="map" role="img" aria-label="Map of central Malta showing the office locations"></div>

  <div class="footer-brand">Falzon &amp; Grech</div>
  <h4 class="col-title" style="left:893px;width:228px">Meeting Hours</h4>
  <p class="hours-intro">Lorem ipsum is the dummy text of the industry &nbsp;lorem fds fdurei.</p>
  <div class="hours" style="top:150px"><span>Monday-Friday:</span><span>9am to 5pm</span></div>
  <div class="hours" style="top:184px"><span>Saturday:</span><span>10am to 2pm</span></div>
  <div class="hours" style="top:218px;border-bottom:0"><span>Sunday:</span><span>Clised</span></div>
</footer>

<div class="section copyright">
  <div class="strip"><b></b><span>Copyright © 2016 Falzon &amp; Grech Advocates. All Rights Reserved. &nbsp;Disclaimer</span><b></b></div>
</div>

</body>
</html>
```